KVR Biz Cards

We are a property management company that manages luxury level residential estates. As such, we need a business card design that gives a high end feel. The idea at the moment is to list the services offered on the back of the card, and our company information on the front of the card.

Services for the back of the card are as follows:
Professional Property Management service, Home Hosting & Concierge Service, Holliday Home / Income Property Management

```html
<!DOCTYPE html>
<html lang="en">
<head>
<meta charset="utf-8">
<title>KVR Business Cards</title>
<link rel="stylesheet" href="https://fonts.googleapis.com/css2?family=Arimo:wght@400;700&display=swap">
<style>
  :root {
    --backdrop: #2b2b2b;
    --card-black: #0d0a09;
    --card-white: #f4f4f4;
    --gold: #8e5c2c;
    --gold-dark: #5e3a18;
    --ink: #111111;
    --light: #ffffff;
  }
  * { box-sizing: border-box; margin: 0; padding: 0; }
  html, body {
    width: 1200px; height: 900px; overflow: hidden;
    background: var(--backdrop);
    font-family: "Arimo", Arial, sans-serif;
  }
  .stage { position: relative; width: 1200px; height: 900px; }
  .card {
    position: absolute; left: 300px; width: 600px; height: 343px;
    overflow: hidden; box-shadow: 0 18px 40px rgba(0,0,0,.55);
  }

  /* Back: services */
  .card-back { top: 70px; background: var(--card-black); }
  .back-brand {
    position: absolute; right: 40px; top: 52px;
    color: var(--gold); font-weight: 400; font-size: 26px;
  }
  .back-rule {
    position: absolute; right: 40px; top: 112px; width: 300px; height: 1px;
    background: var(--light);
  }
  .services {
    position: absolute; right: 40px; top: 130px; text-align: right; color: var(--gold);
  }
  .services h2 { font-size: 19px; font-weight: 700; letter-spacing: .5px; margin-bottom: 8px; }
  .services li { list-style: none; font-size: 14.5px; line-height: 1.55; }

  /* Front: contact */
  .card-front { top: 470px; background: var(--card-white); }
  .front-dark {
    position: absolute; left: 262px; top: 0; width: 338px; height: 343px;
    background: var(--card-black);
  }
  .ribbon { position: absolute; left: 0; top: 0; width: 600px; height: 343px; }
  .ribbon-text {
    position: absolute; left: 300px; top: 42px; color: var(--ink); line-height: 1.05;
  }
  .ribbon-text .role { font-size: 13px; }
  .ribbon-text .person { font-size: 17px; font-weight: 700; letter-spacing: .5px; }
  .contact {
    position: absolute; left: 300px; color: var(--light); font-size: 14px; line-height: 1.3;
    display: flex; align-items: flex-start; gap: 10px;
  }
  .contact svg { flex: none; margin-top: 2px; }
  .contact-phone { top: 112px; }
  .contact-address { top: 168px; }
  .contact-mail { top: 256px; }
  .contact-web { top: 280px; }

  .front-brand {
    position: absolute; left: 30px; top: 122px; width: 210px; text-align: center;
  }
  .front-brand .brand-name { color: var(--gold); font-weight: 400; font-size: 40px; line-height: 1; }
  .company-name { margin-top: 16px; color: var(--ink); font-weight: 700; font-size: 15px; letter-spacing: .5px; }
  .tagline { color: var(--gold); font-size: 10.5px; margin-top: 4px; }
</style>
</head>
<body>
<main class="stage">

  <section class="card card-back" aria-label="Card back: services">
    <div class="back-brand">KVR</div>
    <div class="back-rule"></div>
    <div class="services">
      <h2>SERVICES</h2>
      <ul>
        <li>Professional Property Management service</li>
        <li>Home Hosting &amp; Concierge Service</li>
        <li>Holliday Home / Income Property Management</li>
      </ul>
    </div>
  </section>

  <section class="card card-front" aria-label="Card front: contact details">
    <div class="front-dark"></div>
    <svg class="ribbon" viewBox="0 0 600 343" aria-hidden="true">
      <polygon points="262,96 292,96 292,112" fill="var(--gold-dark)"/>
      <polygon points="262,30 600,30 600,96 262,96 250,63" fill="var(--gold)"/>
    </svg>
    <div class="ribbon-text">
      <div class="role">Director</div>
      <div class="person">JOHN SMITH</div>
    </div>

    <div class="contact contact-phone">
      <svg width="14" height="14" viewBox="0 0 24 24"><path fill="var(--gold)" d="M6.6 10.8a15 15 0 0 0 6.6 6.6l2.2-2.2a1 1 0 0 1 1-.25 11.4 11.4 0 0 0 3.6.6 1 1 0 0 1 1 1V20a1 1 0 0 1-1 1A17 17 0 0 1 3 4a1 1 0 0 1 1-1h3.5a1 1 0 0 1 1 1c0 1.250.2 2.45.6 3.6a1 1 0 0 1-.25 1z"/></svg>
      <span>(00) 0000 0000</span>
    </div>
    <div class="contact contact-address">
      <svg width="14" height="14" viewBox="0 0 24 24"><path fill="var(--gold)" d="M12 2a7 7 0 0 0-7 7c0 5 7 13 7 13s7-8 7-13a7 7 0 0 0-7-7zm0 9.5A2.5 2.5 0 1 1 12 6.5a2.5 2.5 0 0 1 0 5z"/></svg>
      <span>99 dummy city<br>dummy place,<br>00 Dummy Land</span>
    </div>
    <div class="contact contact-mail">
      <svg width="14" height="14" viewBox="0 0 24 24"><path fill="var(--gold)" d="M3 5h18a1 1 0 0 1 1 1v12a1 1 0 0 1-1 1H3a1 1 0 0 1-1-1V6a1 1 0 0 1 1-1zm9 7 8-5H4z"/></svg>
      <span>john@kvr.com</span>
    </div>
    <div class="contact contact-web">
      <svg width="14" height="14" viewBox="0 0 24 24"><circle cx="12" cy="12" r="9" fill="none" stroke="var(--gold)" stroke-width="2"/><path d="M3 12h18M12 3c3 3 3 15 0 18M12 3c-3 3-3 15 0 18" fill="none" stroke="var(--gold)" stroke-width="1.6"/></svg>
      <span>www.kvr.com</span>
    </div>

    <div class="front-brand">
      <div class="brand-name">KVR</div>
      <div class="company-name">KAVORA MANAGEMENT</div>
      <div class="tagline">Crafted to Bring You Calm at Every Home</div>
    </div>
  </section>

</main>
</body>
</html>
```